Business Cards for Corvantis LLC

We need business cards for a new company called “Corvantis LLC”. This is a technology process improvement company providing a comprehensive assessment of the technology used to run their business. The documentation and review process delivers the visibility and reassurance they need to protect their business and plan for the future. The product is called “Halvorne Ledgerwork”. Our primary target is small-medium size businesses, with the deliverables going to the decision maker. We would like to see the designs use the color blue. Our tag line is PROTECT YOUR BUSINESS · TAKE CONTROL OF IT.

Industry/Entity Type

Business

Contact Information for Business Card

Tag line should be on back of card - it does not have to be upper case.

Requirements
Must have
• Please use information when laying out card:
• Name: Darnell Pruitt
• Title: Partner
• Phone Number: (877)555-0143
• Email: dell@corvantisllc.com
• Website: http://corvantisllc.com

```html
<!DOCTYPE html>
<html lang="en">
<head>
<meta charset="utf-8">
<title>Corvantis LLC — Business Card</title>
<link rel="stylesheet" href="https://fonts.googleapis.com/css2?family=Michroma&family=Open+Sans:wght@400;600&display=swap">
<style>
  :root {
    --page-bg: #e4e6ea;
    --card-bg: #f5f6f8;
    --brand-blue: #2f7dc4;
    --brand-blue-deep: #2a68a8;
    --panel-edge: #8d9096;
    --text-grey: #7b7d80;
    --text-dark: #3b3d40;
    --on-blue: #ffffff;
  }
  * { box-sizing: border-box; margin: 0; padding: 0; }
  html, body {
    width: 1200px; height: 900px; overflow: hidden;
    background: var(--page-bg);
  }
  .business-card {
    position: absolute; left: 120px; top: 155px;
    width: 960px; height: 590px;
    background: var(--card-bg);
    border-radius: 20px;
    overflow: hidden;
    box-shadow: 0 10px 30px rgba(0,0,0,0.12);
    font-family: "Open Sans", sans-serif;
  }
  .contact-panel {
    position: absolute; inset: 0; width: 100%; height: 100%;
  }
  .brand-lockup {
    position: absolute; left: 48px; top: 150px;
    display: flex; align-items: center; gap: 18px;
  }
  .brand-square {
    width: 34px; height: 34px; background: var(--brand-blue);
  }
  .brand-name {
    font-family: "Michroma", sans-serif;
    font-size: 36px; color: var(--brand-blue); letter-spacing: 1px;
  }
  .holder-name {
    position: absolute; left: 55px; top: 318px;
    font-family: "Michroma", sans-serif;
    font-size: 31px; color: var(--brand-blue); letter-spacing: 1px;
    text-transform: uppercase;
  }
  .holder-title {
    position: absolute; left: 55px; top: 370px;
    font-size: 22px; color: var(--text-dark);
  }
  .tagline {
    position: absolute; left: 55px; top: 450px;
    font-family: "Michroma", sans-serif;
    font-size: 26px; line-height: 50px; color: var(--text-grey);
    text-transform: uppercase; letter-spacing: 1px;
  }
  .contact-list {
    position: absolute; right: 34px; top: 225px;
    list-style: none; text-align: right;
    color: var(--on-blue); font-size: 22px; line-height: 35px;
  }
  .contact-list li { display: flex; justify-content: flex-end; align-items: center; gap: 10px; }
  .contact-icon { width: 17px; height: 17px; fill: var(--on-blue); }
</style>
</head>
<body>
  <article class="business-card">
    <svg class="contact-panel" viewBox="0 0 650 400" preserveAspectRatio="none" aria-hidden="true">
      <defs>
        <linearGradient id="panelBlue" x1="0" y1="0" x2="1" y2="1">
          <stop offset="0" stop-color="#4a92d2"/>
          <stop offset="1" stop-color="#2a68a8"/>
        </linearGradient>
      </defs>
      <path fill="var(--panel-edge)" d="M552,0 L650,0 L650,400 L510,400 C496,380 496,342 510,320 C470,316 385,305 380,240 L380,200 C380,160 410,138 437,118 Z"/>
      <path fill="url(#panelBlue)" d="M562,0 L650,0 L650,400 L520,400 C506,380 506,342 520,318 C480,314 396,304 391,240 L391,202 C391,164 420,142 446,122 Z"/>
    </svg>

    <div class="brand-lockup">
      <span class="brand-square"></span>
      <span class="brand-name">CORVANTIS LLC</span>
    </div>

    <h1 class="holder-name">Darnell Pruitt</h1>
    <p class="holder-title">Partner</p>

    <p class="tagline">Protect your business<br>Take control of it.</p>

    <ul class="contact-list">
      <li>(877)555-0143
        <svg class="contact-icon" viewBox="0 0 24 24"><path d="M6.6 10.8a15.1 15.1 0 0 0 6.6 6.6l2.2-2.2a1 1 0 0 1 1-.25 11.4 11.4 0 0 0 3.6.57 1 1 0 0 1 1 1V20a1 1 0 0 1-1 1A17 17 0 0 1 3 4a1 1 0 0 1 1-1h3.5a1 1 0 0 1 1 1c0 1.25.2 2.45.57 3.57a1 1 0 0 1-.25 1z"/></svg>
      </li>
      <li>dell@corvantisllc.com
        <svg class="contact-icon" viewBox="0 0 24 24"><path d="M2 5h20v14H2z M3.5 6.5 12 13l8.5-6.5" fill="none" stroke="#fff" stroke-width="2"/><path d="M3 6h18L12 13z"/></svg>
      </li>
      <li>http://corvantisllc.com
        <svg class="contact-icon" viewBox="0 0 24 24"><circle cx="12" cy="12" r="10"/><path d="M2 12h20M12 2c3 3 3 17 0 20M12 2c-3 3-3 17 0 20" fill="none" stroke="#2f7dc4" stroke-width="1.6"/></svg>
      </li>
    </ul>
  </article>
</body>
</html>
```